Webdesign für Naturheilpraktiker gesucht
Zielgruppe
Ich arbeite im Gesundheitswesen als Naturheilpraktiker Traditionell Tibetische Medizin.
Verfüge aber über verschiedene Anwendungstechniken.
Die Zielgruppe sind alle Menschen die mehr als nur klassische Medizin wollen, die mit der klassischen Schulmedizin nicht mehr weiter kommen und einen alternativen Weg suchen. Menschen die neben der Schulmedizin noch einen anderen Weg suchen.
Menschen im Wellness und Fitnessbereich.
Ernährungsbewusste Menschen.
Sportler allgemein da ich über eine neue Technik verfüge (KERVO) die erst auf den Markt kommt und mit der verschiedene Beschwerden gelindert werden können.
Grob gesagt alles was mit Medizin, Komplementärmedizin, Gesundheit, Wellness, Sport usw zu tun hat.
Kompetenzen der Traditionell Tibetische Medizin:
- Massage als Gesundheitssystem oder als Wellness
- Ernährungsberatung
- tibetisches Yoga
- Lebensberatung
- Familienstellen
Aufgabenstellung
Der Firmennamen und das Logo bestehen.
In der Tradition der tibetischen Medizin ist vor allem Blau (Medizin Buddha) die Farben sind aber frei wählbar.
Es soll Vertrautheit, Geborgenheit und Wärme ausstrahlen.
Nicht zu feminin erscheinen.
Einfach ein paar Ideen
http://massagepraxis-wolfrin.example
http://www.himalheilkunde.example

```html
<!DOCTYPE html>
<html lang="de">
<head>
<meta charset="utf-8">
<title>Kontakt – SONAMVITA</title>
<link href="https://fonts.googleapis.com/css2?family=Open+Sans:wght@400;600;700&family=Josefin+Sans:wght@400&display=swap" rel="stylesheet">
<style>
:root{
  --blue:#2b5c9b;
  --teal:#2fb597;
  --text:#4a4a52;
  --muted:#6a6a72;
  --page:#ebebf0;
  --field-border:#d4d6e0;
  --footer:#4c4c4c;
  --footer-text:#6a6a6a;
  --white:#ffffff;
}
*{box-sizing:border-box;margin:0;padding:0}
html,body{width:1200px;height:936px;overflow:hidden}
body{font-family:"Open Sans",Arial,sans-serif;background:var(--page);color:var(--text);position:relative}

.hero{position:absolute;left:0;top:0;width:1200px;height:246px;overflow:hidden}
.hero-photo{position:absolute;inset:0;
  background:
    radial-gradient(ellipse 260px 180px at 170px 60px,rgba(255,236,170,.95),rgba(255,236,170,0) 70%),
    linear-gradient(180deg,#d9dde4 0%,#e2dccb 30%,#cfc4ad 60%,#c8bba4 100%);}
.hero-photo::after{content:"";position:absolute;right:0;bottom:0;width:380px;height:200px;
  background:linear-gradient(160deg,rgba(190,160,120,0) 20%,rgba(200,150,110,.55) 70%,rgba(230,120,90,.5) 100%)}
.hero-veil{position:absolute;inset:0;background:rgba(255,255,255,.35)}

.brand{position:absolute;left:262px;top:10px;width:76px;height:50px;display:flex;flex-direction:column;align-items:center;gap:5px}
.brand-dot{width:26px;height:26px;border-radius:50%;background:var(--blue)}
.brand-name{font-family:"Open Sans",Arial,sans-serif;font-weight:700;font-size:7px;letter-spacing:1.6px;color:var(--blue)}

.nav{position:absolute;top:25px;right:235px;display:flex;align-items:center;font-family:"Josefin Sans",Arial,sans-serif;font-size:7px;letter-spacing:.4px;color:#3c3c44}
.nav a{color:inherit;text-decoration:none}
.nav .sep{width:3px;height:3px;border-radius:50%;background:#a9aebb;margin:0 8.5px}

.page-title{position:absolute;top:154px;left:0;width:1200px;text-align:center;font-weight:600;font-size:28px;color:#3f3f40}
.divider{position:absolute;display:flex;align-items:center;gap:5px}
.divider .line{width:23px;height:1px;background:var(--teal)}
.divider .mark{width:12px;height:12px;border-radius:50%;border:1.5px solid var(--teal)}
.divider-hero{top:198px;left:564px}

.col-title{position:absolute;top:283px;font-size:13px;font-weight:400;color:var(--blue)}
.col-left{left:235px}
.col-right{left:615px}
.divider-left{top:316px;left:235px}
.divider-right{top:316px;left:615px}

.intro,.outro{position:absolute;left:235px;width:350px;font-size:8px;line-height:12.6px;color:var(--text)}
.intro{top:357px}
.outro{top:546px;width:340px}

.contact-list{position:absolute;left:235px;top:446px;list-style:none;font-size:8px;color:var(--text)}
.contact-list li{display:flex;align-items:center;height:15.1px}
.contact-list svg{width:10px;height:10px;margin-right:13px;stroke:var(--blue);fill:none;stroke-width:1.1}

.form label{position:absolute;font-size:8px;color:var(--text)}
.form label .req{color:var(--blue)}
.field{position:absolute;height:26px;background:var(--page);border:1px solid var(--field-border)}
.field-message{height:150px}
.btn{position:absolute;left:615px;top:649px;width:65px;height:25px;border:1px solid #cfd2dc;border-radius:13px;background:var(--white);color:var(--blue);font-family:"Open Sans",Arial,sans-serif;font-weight:700;font-size:7px;letter-spacing:.4px}

.footer{position:absolute;left:0;top:716px;width:1200px;height:220px;background:var(--footer)}
.footer-brand{position:absolute;top:50px;left:0;width:1200px;display:flex;justify-content:center;align-items:center;gap:8px}
.footer-brand .dot{width:22px;height:22px;border-radius:50%;background:#d8d8d8}
.footer-brand .name{font-weight:700;font-size:12px;letter-spacing:2px;color:#d8d8d8}
.social{position:absolute;top:124px;left:510px;display:flex;gap:9px}
.social span{width:29px;height:29px;border-radius:50%;background:var(--white)}
.copyright{position:absolute;top:181px;width:1200px;text-align:center;font-size:8px;color:var(--footer-text)}
.to-top{position:absolute;left:1157px;top:881px;width:30px;height:30px;border:1px solid var(--white);display:flex;align-items:center;justify-content:center}
</style>
</head>
<body>

<header class="hero">
  <div class="hero-photo" role="img" aria-label="Sonnige Panoramaansicht einer Bergstadt mit Palast auf dem Hügel und Gebetsfahnen"></div>
  <div class="hero-veil"></div>
  <div class="brand"><span class="brand-dot"></span><span class="brand-name">SONAMVITA</span></div>
  <nav class="nav">
    <a href="#">HOME</a><span class="sep"></span>
    <a href="#">ÜBER MICH</a><span class="sep"></span>
    <a href="#">TIBETISCHE MEDIZIN</a><span class="sep"></span>
    <a href="#">ANGEBOT</a><span class="sep"></span>
    <a href="#">TERMINE</a><span class="sep"></span>
    <a href="#">KONTAKT</a>
  </nav>
  <h1 class="page-title">Kontakt</h1>
  <div class="divider divider-hero"><span class="line"></span><span class="mark" role="img" aria-label="Zierelement"></span><span class="line"></span></div>
</header>

<main>
  <h2 class="col-title col-left">Kontaktdaten</h2>
  <div class="divider divider-left"><span class="line"></span><span class="mark" role="img" aria-label="Zierelement"></span><span class="line"></span></div>
  <p class="intro">Lorem ipsum dolor sit amet, consetetur sadipscing elitr, sed diam nonumy eirmod tempor invidunt ut labore et.<br>Dolore magna aliquyam erat, sed diam voluptua. At vero eos et accusam et justo duo dolores et ea rebum.</p>

  <ul class="contact-list">
    <li><svg viewBox="0 0 10 10"><path d="M9 1L1 4.5l3.8.8.8 3.8z" fill="#2b5c9b"/></svg>Musterstraße 1 - 12345 Musterort</li>
    <li><svg viewBox="0 0 10 10"><rect x="2.5" y=".6" width="5" height="8.8" rx="1"/><line x1="4.4" y1="8" x2="5.6" y2="8"/></svg>0123 456 7890</li>
    <li><svg viewBox="0 0 10 10"><rect x="2.5" y=".8" width="5" height="2.6"/><rect x=".7" y="3.4" width="8.6" height="3.8" rx=".6"/><rect x="2.5" y="6" width="5" height="3.2"/></svg>0123 456 7890</li>
    <li><svg viewBox="0 0 10 10"><path d="M.8 4l4.2-3 4.2 3v5H.8z"/><path d="M.8 4l4.2 3 4.2-3"/></svg>mail@website.com</li>
    <li><svg viewBox="0 0 10 10"><circle cx="5" cy="5" r="4.2"/><ellipse cx="5" cy="5" rx="1.8" ry="4.2"/><line x1=".8" y1="5" x2="9.2" y2="5"/></svg>www.website.com</li>
  </ul>

  <p class="outro">In ultricies quam sem, suscipit blandit risus tempor ac. Donec sed odio quam. Morbi sit amet dapibus est, vel aliquam nunc. Aliqu am in maximus lorem. Vivamus sit amet commodo orci, congue efficitur magna. Nullam eu porta tortor.</p>

  <h2 class="col-title col-right">Kontaktformular</h2>
  <div class="divider divider-right"><span class="line"></span><span class="mark" role="img" aria-label="Zierelement"></span><span class="line"></span></div>

  <form class="form">
    <label style="left:615px;top:357px">Name <span class="req">*</span></label>
    <div class="field" style="left:615px;top:375px;width:168px"></div>
    <label style="left:798px;top:357px">Email <span class="req">*</span></label>
    <div class="field" style="left:798px;top:375px;width:167px"></div>
    <label style="left:615px;top:410px">Telefonnummer</label>
    <div class="field" style="left:615px;top:428px;width:168px"></div>
    <label style="left:798px;top:410px">Betreff <span class="req">*</span></label>
    <div class="field" style="left:798px;top:428px;width:167px"></div>
    <label style="left:615px;top:463px">Nachricht <span class="req">*</span></label>
    <div class="field field-message" style="left:615px;top:481px;width:350px"></div>
    <button class="btn" type="button">SENDEN</button>
  </form>
</main>

<footer class="footer">
  <div class="footer-brand"><span class="dot"></span><span class="name">SONAMVITA</span></div>
  <div class="social"><span></span><span></span><span></span><span></span><span></span></div>
  <p class="copyright">© 2018 SONAMVITA. Alle Rechte vorbehalten</p>
</footer>

<a class="to-top" href="#" aria-label="Nach oben"><svg width="8" height="6" viewBox="0 0 8 6"><path d="M1 5l3-3 3 3" stroke="#fff" stroke-width="1.4" fill="none"/></svg></a>

</body>
</html>
```